Security Camera Sign

14” high x 11” wide Color: Blue, Yellow, Black and white

Make the sign vertical
Replace red with blue
WARNING: Black over yellow
These premises are protected by Closed Circuit Television: On white
Images are recorded for crime prevention and public safety. Unauthorized access, theft or vandalism will result in prosecution: On Blue

Target Market(s)

Outdoor commercial building

Industry/Entity Type

Security

Requirements
Nice to have
• I would like the sign stand out. If you need more colors? Thanks Ok

```html
<!DOCTYPE html>
<html lang="en">
<head>
<meta charset="utf-8">
<title>Security Camera Sign</title>
<link href="https://fonts.googleapis.com/css2?family=PT+Sans:wght@700&family=PT+Sans+Narrow:wght@700&display=swap" rel="stylesheet">
<style>
  :root {
    --page-bg: #ececec;
    --sign-blue-dark: #1f2f7a;
    --sign-blue: #24409a;
    --sign-blue-light: #1f6bc2;
    --trim-orange: #f2a311;
    --band-yellow: #ffe000;
    --band-orange: #f5a60f;
    --ink: #231f20;
    --panel-white: #ffffff;
    --panel-grey: #d9d9d9;
    --camera-light: #f1f1f1;
    --camera-mid: #c9cacc;
    --text-white: #ffffff;
  }
  html, body {
    margin: 0;
    padding: 0;
    width: 1200px;
    height: 789px;
    overflow: hidden;
    background: var(--page-bg);
  }
  .canvas {
    position: relative;
    width: 1200px;
    height: 789px;
  }
  .sign {
    position: absolute;
    left: 367px;
    top: 98px;
    width: 466px;
    height: 592px;
    border-radius: 30px;
    background: linear-gradient(160deg, var(--sign-blue-light) 0%, var(--sign-blue) 45%, var(--sign-blue-dark) 100%);
    box-shadow: 0 0 0 1px #17245f;
  }
  .sign-trim {
    position: absolute;
    inset: 7px;
    border: 3px solid var(--trim-orange);
    border-radius: 24px;
  }
  .warning-band {
    position: absolute;
    left: 28px;
    top: 27px;
    width: 410px;
    height: 72px;
    border-radius: 14px;
    background: linear-gradient(90deg, var(--band-orange) 0%, var(--band-yellow) 30%, var(--band-yellow) 70%, var(--band-orange) 100%);
    display: flex;
    align-items: center;
    justify-content: center;
  }
  .warning-title {
    margin: 0;
    font-family: "PT Sans", sans-serif;
    font-weight: 700;
    font-size: 76px;
    line-height: 1;
    letter-spacing: 1px;
    color: var(--ink);
  }
  .notice-panel {
    position: absolute;
    left: 23px;
    top: 118px;
    width: 418px;
    height: 374px;
    background: radial-gradient(ellipse at 70% 50%, var(--panel-white) 0%, #f4f4f4 55%, var(--panel-grey) 100%);
    border: 2px solid #b8b8b8;
    box-sizing: border-box;
    overflow: hidden;
  }
  .camera-illustration {
    position: absolute;
    left: 78px;
    top: 16px;
    width: 338px;
    height: 322px;
  }
  .notice-headline {
    position: absolute;
    left: 12px;
    top: 160px;
    margin: 0;
    font-family: "PT Sans Narrow", sans-serif;
    font-weight: 700;
    font-size: 37px;
    line-height: 42px;
    color: var(--ink);
    text-transform: uppercase;
  }
  .notice-detail {
    position: absolute;
    left: 30px;
    right: 30px;
    top: 502px;
    margin: 0;
    font-family: "PT Sans Narrow", sans-serif;
    font-weight: 700;
    font-size: 19.5px;
    line-height: 24px;
    text-align: center;
    color: var(--text-white);
    text-transform: uppercase;
  }
</style>
</head>
<body>
<main class="canvas">
  <section class="sign" aria-label="CCTV warning sign">
    <div class="sign-trim"></div>
    <div class="warning-band">
      <h1 class="warning-title">WARNING</h1>
    </div>
    <div class="notice-panel">
      <svg class="camera-illustration" viewBox="0 0 338 322" role="img" aria-label="Illustration of a white wall-mounted security camera">
        <defs>
          <linearGradient id="cameraTone" x1="0" y1="0" x2="1" y2="1">
            <stop offset="0" stop-color="var(--camera-light)"/>
            <stop offset="1" stop-color="var(--camera-mid)"/>
          </linearGradient>
        </defs>
        <rect x="0" y="0" width="338" height="322" rx="24" fill="url(#cameraTone)" opacity="0.75"/>
      </svg>
      <h2 class="notice-headline">These<br>premises are<br>protected by<br>closed circuit<br>television</h2>
    </div>
    <p class="notice-detail">Images are recorded for crime prevention and<br>public safety. Unauthorized access, theft or<br>vandalism will result in prosecution</p>
  </section>
</main>
</body>
</html>
```